Landingpage design

We need a landingpage for a chatterloop add campaign. We sell socks made of bamboo in super quality. Our customers loves us, and we have a 5 heart rating at opinivo.com.

We want to create a add campaign targeted new customers, and the offer is that they can buy 1 pair of bamboo socks as a test, for only 20 DKK (2,7 Euro) including shipment. Our webpage is www.lintora.dk, landingpage should be built i Pagmoro, a wysiwyg editor. based on their template. like:
https://lintora.pagmoro.com/13844-sales-page
https://lintora.pagmoro.com/13696-sales-page
https://lintora.pagmoro.com/13845-sales-page

You don't have to follow the templates 100% if you have better ideas. We have an account for snapquarry, so please get stockphotos from here.

Bamboo socks has a lot of great selling points, you can see a good desciption here:
https://tovelin.com/us/why-bamboo

We expect you to have experience in landingpage design, and expect to end up with 2 landingpages we can splittest on.

This is the first of a number of landingpages we need in the future, so for the right person there will be plenty of more work.

Target Market(s)

Denmark

Industry/Entity Type

E-Commerce

Number of Pages Required

2 page

Colors

Designer to choose colors to be used in the design.

Requirements
Must have
• A great selling page, showing all the great things with bamboo socks. It should be supplied with good packshots from snapquarry.com

```html
<!DOCTYPE html>
<html lang="da">
<head>
<meta charset="utf-8">
<title>Lintora – Bambusstrømper</title>
<link rel="stylesheet" href="https://fonts.googleapis.com/css2?family=Poppins:wght@300;400;500;600;700&display=swap">
<style>
:root{
  --orange:#f6a623;
  --ink:#1d1d1d;
  --text:#555;
  --muted:#8a8a8a;
  --line:#e6e6e6;
  --card:#f4f4f4;
  --white:#fff;
}
*{box-sizing:border-box;margin:0;padding:0}
html,body{width:1200px;height:3108px;overflow:hidden}
body{font-family:"Poppins",sans-serif;color:var(--text);background:var(--white);position:relative}

/* header */
.site-header{position:absolute;top:0;left:0;width:1200px;height:104px;background:var(--white)}
.brand{position:absolute;display:flex;align-items:center;gap:14px}
.site-header .brand{left:80px;top:24px}
.brand-mark{width:56px;height:56px;background:var(--ink);flex:none}
.brand-name{font-size:19px;font-weight:600;color:var(--ink);line-height:1.3;white-space:nowrap}
.main-nav{position:absolute;left:440px;top:58px;display:flex;gap:30px;font-size:13px;color:var(--ink);white-space:nowrap}
.social{position:absolute;right:80px;top:24px;display:flex;gap:12px}
.social span{width:18px;height:18px;border-radius:50%;background:var(--orange)}

/* hero */
.hero{position:absolute;top:104px;left:0;width:1200px;height:612px;background:linear-gradient(100deg,#d9d2c8 0%,#efe9e1 40%,#f6f3ee 70%,#e9e4dc 100%)}
.hero-title{position:absolute;right:90px;top:340px;text-align:right;color:var(--white)}
.hero-title h1{font-size:74px;font-weight:400;line-height:1.05;text-shadow:0 2px 8px rgba(0,0,0,.15)}
.hero-title p{font-size:56px;font-weight:300;line-height:1.2;text-shadow:0 2px 8px rgba(0,0,0,.1)}

/* welcome */
.welcome{position:absolute;top:780px;left:100px;width:1000px;text-align:center}
.welcome h2{font-size:48px;font-weight:400;color:var(--ink);letter-spacing:1px;line-height:1.2}
.welcome hr{width:60px;border:0;border-top:3px solid var(--orange);margin:16px auto 30px}
.welcome p{font-size:14px;line-height:1.9;color:var(--muted)}

/* offer band */
.offer{position:absolute;top:1070px;left:80px;width:1040px;height:160px;background:var(--orange)}
.offer-sock{position:absolute;left:30px;top:-30px;width:170px;height:170px;border-radius:40px 40px 60px 20px;background:linear-gradient(150deg,#3aa0e6 0%,#1e6fb8 70%,#165a99 100%)}
.offer-text{position:absolute;left:250px;top:36px;color:var(--ink)}
.offer-text h3{font-size:40px;font-weight:400;line-height:1.1}
.offer-text p{font-size:28px;font-weight:300;line-height:1.4}
.price-badge{position:absolute;right:40px;top:-30px;width:220px;height:220px;border-radius:50%;background:var(--white);border:10px solid var(--orange);text-align:center;color:var(--ink)}
.price-badge .lead{display:block;background:var(--orange);color:var(--white);font-size:20px;margin:20px 30px 0;border-radius:20px}
.price-badge strong{display:block;font-size:84px;font-weight:700;line-height:1}
.price-badge .cur{font-size:28px;font-weight:600}

/* products */
.products{position:absolute;top:1300px;left:88px;width:1024px;display:grid;grid-template-columns:repeat(4,232px);column-gap:32px;row-gap:52px}
.product-photo{height:260px;background:var(--card);position:relative}
.tag{position:absolute;left:8px;top:8px;width:66px;height:50px;border-radius:50%;background:#5d5d5d;color:var(--white);font-size:9px;text-align:center;padding-top:13px;line-height:1.3}
.save{position:absolute;right:8px;bottom:8px;width:40px;height:40px;border-radius:50%;background:var(--orange);color:var(--white);font-size:10px;display:flex;align-items:center;justify-content:center}
.product-info{padding:14px 4px 0;font-size:12px;line-height:1.5;color:var(--muted)}
.product-meta{display:flex;justify-content:space-between;align-items:center;margin-top:8px}
.product-price{color:var(--orange);font-size:20px;font-weight:500}
.buy{display:block;margin-top:10px;height:34px;line-height:34px;text-align:center;background:var(--orange);color:var(--white);font-size:14px;font-weight:500}

/* testimonial */
.testimonial{position:absolute;top:2250px;left:0;width:1200px;height:450px;background:linear-gradient(180deg,#1a1715 0%,#2b2421 55%,#1c1816 100%);text-align:center;color:var(--white)}
.testimonial h2{font-size:44px;font-weight:300;margin-top:52px}
.quote-icon{width:40px;height:40px;border-radius:50%;background:var(--orange);margin:30px auto 24px;display:flex;align-items:center;justify-content:center}
.testimonial p{font-size:14px;line-height:2;color:#cfcfcf;width:900px;margin:0 auto}
.client{margin-top:28px;font-size:14px;font-weight:500;letter-spacing:1px}
.client small{display:block;font-size:11px;color:#aaa;font-weight:400}
.avatars{position:absolute;top:2610px;left:0;width:1200px;display:flex;justify-content:center;align-items:center;gap:44px}
.avatar{border-radius:50%;background:linear-gradient(160deg,#c9b8a6,#8d7a6b);border:6px solid var(--white)}
.avatar.sm{width:128px;height:128px}
.avatar.lg{width:170px;height:170px;border-color:var(--orange)}

/* footer */
.site-footer{position:absolute;top:2840px;left:0;width:1200px;height:220px}
.site-footer .brand{left:80px;top:20px}
.footer-phone{position:absolute;left:80px;top:120px;font-size:13px;color:var(--ink)}
.footer-col{position:absolute;top:20px;font-size:13px;color:var(--ink)}
.footer-col h4{font-size:14px;font-weight:500;margin-bottom:18px}
.footer-col li{list-style:none;margin-bottom:12px;color:var(--text)}
.footer-social{position:absolute;right:110px;top:20px;display:grid;grid-template-columns:40px 40px;gap:22px}
.footer-social span{width:40px;height:40px;border-radius:50%;background:var(--orange)}
.copyright{position:absolute;top:3060px;left:0;width:1200px;height:48px;border-top:1px solid var(--line);text-align:center;line-height:48px;font-size:12px;color:var(--muted)}
</style>
</head>
<body>

<header class="site-header">
  <div class="brand">
    <span class="brand-mark"></span>
    <div class="brand-name">Lintora – basics i bambus<br>lige til og enkelt</div>
  </div>
  <nav class="main-nav">
    <span>Forsiden</span><span>Produkter</span><span>Abonnement</span><span>Om Bambus</span><span>Hjælp</span><span>Forhandler</span>
  </nav>
  <div class="social"><span></span><span></span><span></span><span></span><span></span></div>
</header>

<section class="hero" role="img" aria-label="Kvinde i strikket trøje og bambusstrømper med en kop kaffe og en tablet">
  <div class="hero-title">
    <h1>Keep cool</h1>
    <p>Wear Lintora</p>
  </div>
</section>

<section class="welcome">
  <h2>WELCOME TO LINTORA</h2>
  <hr>
  <p>Bamboo clothing? Before you met us you had probably never even heard of such a thing. Bamboo is more famous for being panda food and is not (yet) associated with clothes. But this is about to change because bamboo clothing is getting more popular by the day. We will tell you here why we fell in love with bamboo, and how it is possible to make clothing from bamboo stems.</p>
</section>

<section class="offer">
  <div class="offer-sock" role="img" aria-label="Blå bambusstrømpe med orange hæl"></div>
  <div class="offer-text">
    <h3>As a test</h3>
    <p>Buy 1 pair of bamboo socks</p>
  </div>
  <div class="price-badge">
    <span class="lead">for only</span>
    <strong>20</strong>
    <span class="cur">DKK</span>
  </div>
</section>

<section class="products">
  <article class="product">
    <div class="product-photo" role="img" aria-label="Sort bambusstrømpe"><span class="tag">7% rabat<br>spar nu</span><span class="save">-7%</span></div>
    <div class="product-info">Bløde sorte bambusstrømper<br>kun til pris af hverdag
      <div class="product-meta"><span class="product-price">$260.00</span><svg width="60" height="10"><g fill="#333"><circle cx="5" cy="5" r="4"/><circle cx="17" cy="5" r="4"/><circle cx="29" cy="5" r="4"/><circle cx="41" cy="5" r="4"/></g><circle cx="53" cy="5" r="4" fill="#ccc"/></svg></div>
    </div>
    <span class="buy">Buy This Product</span>
  </article>
  <article class="product">
    <div class="product-photo" role="img" aria-label="Sorte og hvide bambus t-shirts"><span class="tag">7% rabat<br>spar nu</span><span class="save">-7%</span></div>
    <div class="product-info">Bløde bambus t-shirts i sæt<br>kun til pris af hverdag
      <div class="product-meta"><span class="product-price">$260.00</span><svg width="60" height="10"><g fill="#333"><circle cx="5" cy="5" r="4"/><circle cx="17" cy="5" r="4"/><circle cx="29" cy="5" r="4"/><circle cx="41" cy="5" r="4"/></g><circle cx="53" cy="5" r="4" fill="#ccc"/></svg></div>
    </div>
    <span class="buy">Buy This Product</span>
  </article>
  <article class="product">
    <div class="product-photo" role="img" aria-label="Undertøj og toppe i bambus"><span class="tag">7% rabat<br>spar nu</span><span class="save">-7%</span></div>
    <div class="product-info">Bløde bambus undertøj til hende<br>kun til pris af hverdag
      <div class="product-meta"><span class="product-price">$260.00</span><svg width="60" height="10"><g fill="#333"><circle cx="5" cy="5" r="4"/><circle cx="17" cy="5" r="4"/><circle cx="29" cy="5" r="4"/><circle cx="41" cy="5" r="4"/></g><circle cx="53" cy="5" r="4" fill="#ccc"/></svg></div>
    </div>
    <span class="buy">Buy This Product</span>
  </article>
  <article class="product">
    <div class="product-photo" role="img" aria-label="Seks par sorte bambusstrømper"><span class="tag">7% rabat<br>spar nu</span><span class="save">-7%</span></div>
    <div class="product-info">Bløde sorte strømper seks par<br>kun til pris af hverdag
      <div class="product-meta"><span class="product-price">$260.00</span><svg width="60" height="10"><g fill="#333"><circle cx="5" cy="5" r="4"/><circle cx="17" cy="5" r="4"/><circle cx="29" cy="5" r="4"/><circle cx="41" cy="5" r="4"/></g><circle cx="53" cy="5" r="4" fill="#ccc"/></svg></div>
    </div>
    <span class="buy">Buy This Product</span>
  </article>
  <article class="product">
    <div class="product-photo" role="img" aria-label="Hvide trusser i bambus"><span class="tag">7% rabat<br>spar nu</span><span class="save">-7%</span></div>
    <div class="product-info">Bløde hvide bambus trusser<br>kun til pris af hverdag
      <div class="product-meta"><span class="product-price">$260.00</span><svg width="60" height="10"><g fill="#333"><circle cx="5" cy="5" r="4"/><circle cx="17" cy="5" r="4"/><circle cx="29" cy="5" r="4"/><circle cx="41" cy="5" r="4"/></g><circle cx="53" cy="5" r="4" fill="#ccc"/></svg></div>
    </div>
    <span class="buy">Buy This Product</span>
  </article>
  <article class="product">
    <div class="product-photo" role="img" aria-label="Hvid bambus t-shirt"><span class="tag">7% rabat<br>spar nu</span><span class="save">-7%</span></div>
    <div class="product-info">Blød hvid bambus t-shirt<br>kun til pris af hverdag
      <div class="product-meta"><span class="product-price">$260.00</span><svg width="60" height="10"><g fill="#333"><circle cx="5" cy="5" r="4"/><circle cx="17" cy="5" r="4"/><circle cx="29" cy="5" r="4"/><circle cx="41" cy="5" r="4"/></g><circle cx="53" cy="5" r="4" fill="#ccc"/></svg></div>
    </div>
    <span class="buy">Buy This Product</span>
  </article>
  <article class="product">
    <div class="product-photo" role="img" aria-label="Hvid bambus top"><span class="tag">7% rabat<br>spar nu</span><span class="save">-7%</span></div>
    <div class="product-info">Blød hvid bambus top<br>kun til pris af hverdag
      <div class="product-meta"><span class="product-price">$260.00</span><svg width="60" height="10"><g fill="#333"><circle cx="5" cy="5" r="4"/><circle cx="17" cy="5" r="4"/><circle cx="29" cy="5" r="4"/><circle cx="41" cy="5" r="4"/></g><circle cx="53" cy="5" r="4" fill="#ccc"/></svg></div>
    </div>
    <span class="buy">Buy This Product</span>
  </article>
  <article class="product">
    <div class="product-photo" role="img" aria-label="Sort bambus t-shirt"><span class="tag">7% rabat<br>spar nu</span><span class="save">-7%</span></div>
    <div class="product-info">Blød sort bambus t-shirt<br>kun til pris af hverdag
      <div class="product-meta"><span class="product-price">$260.00</span><svg width="60" height="10"><g fill="#333"><circle cx="5" cy="5" r="4"/><circle cx="17" cy="5" r="4"/><circle cx="29" cy="5" r="4"/><circle cx="41" cy="5" r="4"/></g><circle cx="53" cy="5" r="4" fill="#ccc"/></svg></div>
    </div>
    <span class="buy">Buy This Product</span>
  </article>
</section>

<section class="testimonial">
  <h2>Happy Client</h2>
  <div class="quote-icon"><svg width="18" height="14" viewBox="0 0 18 14"><path d="M0 14V8C0 3 3 0 7 0v3C5 3 4 5 4 7h3v7zm10 0V8c0-5 3-8 7-8v3c-2 0-3 2-3 4h3v7z" fill="#fff"/></svg></div>
  <p>It is a long established fact that a reader will be distracted by the readable content of a page when looking at its layout.<br>It is a long established fact that a reader will be distracted by the readable.</p>
  <div class="client">METTE HOLM<small>DIRECTOR</small></div>
</section>
<div class="avatars">
  <span class="avatar sm" role="img" aria-label="Portræt af kunde"></span>
  <span class="avatar lg" role="img" aria-label="Portræt af kunde"></span>
  <span class="avatar sm" role="img" aria-label="Portræt af kunde"></span>
</div>

<footer class="site-footer">
  <div class="brand">
    <span class="brand-mark"></span>
    <div class="brand-name">Lintora – basics i bambus<br>lige til og enkelt</div>
  </div>
  <div class="footer-phone">+45 31 42 77 09</div>
  <div class="footer-col" style="left:500px">
    <h4>Quick Links</h4>
    <ul><li>Home</li><li>Help Center</li></ul>
  </div>
  <div class="footer-col" style="left:740px">
    <h4>Company</h4>
    <ul><li>Contact</li><li>Privacy Policy</li><li>Terms of Service</li></ul>
  </div>
  <div class="footer-social"><span></span><span></span><span></span><span></span></div>
</footer>
<div class="copyright">lintora.com © 2024 All rights reserved</div>

</body>
</html>
```